Business card for a vending machine business

I need a business card for my vending machine business. The name is Kestrel Snackworks, LLC. The card is one-sided, and landscape format. Not portrait.

The information for the card is as follows:

Dana Whitlow
Owner
(555) 314-2907
Kestrelsnackworks.example
Info@kestrelsnackworks.example

I'd like colors and design elements to match what's in my logo and company name. I'd like to have the checkered flag or racing stripe if possible You can use a border if youd like. You can use a background color if it looks nice and doesn't clash with the logo
Use your creativity. But a white background is perfectly fine. The card can be as simple, yet gets the point across to match the company name and logo.

I uploaded a copy of my logo. I also uploaded a businesses card I started to create, but since it was missing something, I gave up. Another upload has a red thunderbolt and the checkerer flag. Those two uploads are for inspiration. Again, please make sure to make the card landscape, not portrait. Thank you, designers. Good luck to all.

```html
<!DOCTYPE html>
<html lang="en">
<head>
<meta charset="utf-8">
<title>Kestrel Snackworks – Business Card</title>
<link href="https://fonts.googleapis.com/css2?family=Lato:wght@400;700;900&display=swap" rel="stylesheet">
<style>
  :root {
    --page-bg: #e6e3e1;
    --card-bg: #f7f7f7;
    --brand-red: #e3141b;
    --ink: #2b2b2b;
    --ink-soft: #3c3c3c;
    --stripe-black: #161616;
    --check-grey: #7c7c7c;
    --ghost-blue: #e4ecf1;
  }
  * { box-sizing: border-box; margin: 0; padding: 0; }
  html, body {
    width: 1200px; height: 734px; overflow: hidden;
    background: var(--page-bg);
    font-family: "Lato", sans-serif;
  }
  .card {
    position: absolute; left: 40px; top: 47px;
    width: 1120px; height: 640px;
    background: var(--card-bg);
    box-shadow: 0 10px 30px rgba(0,0,0,0.18);
    overflow: hidden;
  }
  .mascot-watermark {
    position: absolute; left: 590px; top: 45px;
    width: 470px; height: 430px;
    background: radial-gradient(ellipse 50% 50% at 55% 50%, var(--ghost-blue) 0%, rgba(236,236,236,0.6) 55%, rgba(247,247,247,0) 100%);
    opacity: 0.55;
  }
  .brand {
    position: absolute; left: 81px; top: 296px;
    width: 430px;
    display: flex; align-items: center; gap: 14px;
  }
  .brand-dot {
    width: 22px; height: 22px; border-radius: 50%;
    background: var(--brand-red); flex: none;
  }
  .brand-name {
    font-weight: 900; font-size: 34px; line-height: 1.05;
    color: var(--brand-red); letter-spacing: 0.5px;
  }
  .contact-list {
    position: absolute; left: 80px; top: 428px;
    list-style: none;
  }
  .contact-item {
    display: flex; align-items: center; gap: 16px;
    height: 39px;
    font-size: 24px; color: var(--ink-soft); letter-spacing: 0.8px;
  }
  .contact-icon { width: 22px; height: 22px; flex: none; }
  .person {
    position: absolute; right: 75px; top: 426px;
    text-align: right;
  }
  .person-name {
    font-weight: 700; font-size: 48px; line-height: 1;
    color: var(--brand-red); letter-spacing: 0.3px;
  }
  .person-role {
    margin-top: 8px;
    font-size: 25px; color: var(--ink); letter-spacing: 1px;
  }
  .racing-band {
    position: absolute; left: 0; bottom: 0;
    width: 1120px; height: 30px;
    background: linear-gradient(90deg, #8c8c8c 0%, var(--check-grey) 56%, var(--stripe-black) 58%, var(--stripe-black) 100%);
  }
  .flag-corner {
    position: absolute; left: 830px; top: 548px;
    width: 290px; height: 62px;
    background: linear-gradient(90deg, rgba(22,22,22,0.25) 0%, rgba(22,22,22,0.75) 45%, var(--stripe-black) 100%);
    clip-path: polygon(4% 100%, 30% 20%, 100% 30%, 100% 100%);
  }
</style>
</head>
<body>
  <main class="card">
    <div class="mascot-watermark" role="img" aria-label="Faint large mascot illustration: smiling vending machine waving a checkered flag"></div>

    <div class="brand">
      <span class="brand-dot"></span>
      <span class="brand-name">Kestrel Snackworks</span>
    </div>

    <ul class="contact-list">
      <li class="contact-item">
        <svg class="contact-icon" viewBox="0 0 24 24" aria-hidden="true">
          <path fill="var(--brand-red)" d="M6.6 10.8a15.1 15.1 0 0 0 6.6 6.6l2.2-2.2a1 1 0 0 1 1-.25 11.4 11.4 0 0 0 3.6.57 1 1 0 0 1 1 1V20a1 1 0 0 1-1 1A17 17 0 0 1 3 4a1 1 0 0 1 1-1h3.5a1 1 0 0 1 1 1c0 1.25.2 2.45.57 3.57a1 1 0 0 1-.25 1z"/>
        </svg>
        <span>(555) 314-2907</span>
      </li>
      <li class="contact-item">
        <svg class="contact-icon" viewBox="0 0 24 24" aria-hidden="true">
          <rect x="2" y="5" width="20" height="14" fill="var(--brand-red)"/>
          <path d="M2 5l10 8 10-8" fill="none" stroke="#fff" stroke-width="1.6"/>
        </svg>
        <span>Info@kestrelsnackworks.example</span>
      </li>
      <li class="contact-item">
        <svg class="contact-icon" viewBox="0 0 24 24" aria-hidden="true">
          <circle cx="12" cy="12" r="10" fill="var(--brand-red)"/>
          <ellipse cx="12" cy="12" rx="4.5" ry="10" fill="none" stroke="#fff" stroke-width="1.4"/>
          <path d="M2 12h20" stroke="#fff" stroke-width="1.4"/>
        </svg>
        <span>Kestrelsnackworks.example</span>
      </li>
    </ul>

    <div class="person">
      <p class="person-name">DANA WHITLOW</p>
      <p class="person-role">Owner</p>
    </div>

    <div class="flag-corner" role="img" aria-label="Scattered checkered flag squares rising toward the corner"></div>
    <div class="racing-band" role="img" aria-label="Checkered racing band blending into a solid black racing stripe"></div>
  </main>
</body>
</html>
```